Law Offices business card

Hi there, I'll need business card for the Law Offices of Tobin Haskell. The information must convey his strategic approach and quick resolution to complex business litigation needs. Please emphasize Civil Litigation, Corporate Law, Business Governance and Real Estate Law. Tobin has over 25 years of experience in these fields.The card should be modern and edgy and the message should be clear. Please consult his current website for ideas.

Business

```html
<!DOCTYPE html>
<html lang="en">
<head>
<meta charset="utf-8">
<title>Tobin Haskell – Business Card</title>
<link rel="stylesheet" href="https://fonts.googleapis.com/css2?family=Arimo:wght@400;700&display=swap">
<style>
  :root{
    --backdrop:#d9d4cc;
    --card-black:#070707;
    --card-sheen:#1c1c1c;
    --accent-red:#c0504f;
    --text-white:#f2f2f2;
    --text-soft:#d8d8d8;
    --text-muted:#a8a8a8;
    --edge-white:#f4f4f4;
    --edge-grey:#cfcfcf;
  }
  *{box-sizing:border-box;margin:0;padding:0}
  html,body{width:1200px;height:950px;overflow:hidden}
  body{background:var(--backdrop);font-family:"Arimo",Arial,sans-serif;position:relative}

  .card{
    position:absolute;width:620px;height:354px;border-radius:4px;overflow:hidden;
    background:linear-gradient(160deg,var(--card-sheen) 0%,var(--card-black) 45%,var(--card-black) 100%);
    box-shadow:0 18px 40px rgba(0,0,0,.35);
  }

  /* Back side */
  .card-back{left:90px;top:70px}
  .back-name{
    position:absolute;left:0;right:0;top:110px;text-align:center;
    color:var(--accent-red);font-size:30px;font-weight:700;letter-spacing:1px;
  }
  .back-web{
    position:absolute;left:0;right:0;top:192px;display:flex;align-items:center;justify-content:center;gap:14px;
  }
  .back-web .rule{width:70px;height:2px;background:var(--accent-red)}
  .back-web span{color:var(--text-soft);font-size:14px;letter-spacing:5px}
  .practice{
    position:absolute;left:0;right:0;top:262px;text-align:center;
    color:var(--text-soft);font-size:12px;letter-spacing:1.5px;text-transform:uppercase;
  }
  .practice .dot{color:var(--accent-red);margin:0 6px}
  .experience{
    position:absolute;left:0;right:0;top:286px;text-align:center;
    color:var(--text-muted);font-size:12px;letter-spacing:1.5px;
  }

  /* Front side */
  .card-front{left:490px;top:520px}
  .contact{
    position:absolute;right:38px;top:28px;text-align:right;color:var(--text-white);
  }
  .person-name{color:var(--accent-red);font-size:19px;font-weight:700}
  .person-title{font-size:14px;margin-top:3px}
  .address{font-size:13px;line-height:17px;margin-top:18px;margin-right:22px}
  .lines{list-style:none;margin-top:6px}
  .lines li{display:flex;justify-content:flex-end;align-items:center;gap:8px;font-size:13px;line-height:17px}
  .lines li.email{margin-top:6px}
  .lines svg{width:14px;height:14px;fill:var(--accent-red);flex:none}

  .firm{
    position:absolute;left:36px;bottom:78px;color:var(--text-white);
  }
  .firm-small{font-size:12px;letter-spacing:1px;text-transform:uppercase;font-weight:700}
  .firm-name{font-size:30px;font-weight:700;margin-top:4px}

  .edge{
    position:absolute;left:0;right:0;bottom:0;height:52px;
    background:linear-gradient(180deg,var(--edge-white),var(--edge-grey));
    clip-path:polygon(0 70%,60% 70%,60% 0,100% 0,100% 100%,0 100%);
  }
  .web-tab{
    position:absolute;right:0;bottom:38px;width:250px;height:40px;
    background:var(--accent-red);border-top-left-radius:28px;
    color:var(--text-white);font-size:14px;font-weight:700;letter-spacing:3px;
    display:flex;align-items:center;justify-content:center;
  }
</style>
</head>
<body>
  <section class="card card-back" aria-label="Card back">
    <p class="back-name">Tobin Haskell</p>
    <div class="back-web"><i class="rule"></i><span>www.haskell-law.com</span><i class="rule"></i></div>
    <p class="practice">Civil Litigation<span class="dot">•</span>Corporate Law<span class="dot">•</span>Business Governance<span class="dot">•</span>Real Estate Law</p>
    <p class="experience">Over 25 years of strategic, swift resolution</p>
  </section>

  <section class="card card-front" aria-label="Card front">
    <div class="contact">
      <p class="person-name">Ellis Crane</p>
      <p class="person-title">President</p>
      <p class="address">2140 Alder Court<br>Fairbanks, Alaska 99701</p>
      <ul class="lines">
        <li>555 210 4821
          <svg viewBox="0 0 16 16"><path d="M3 1l3 3-1.5 2c1 2 3 4 5 5L11.5 9.5l3 3L13 15C7 14 2 9 1 3z"/></svg></li>
        <li>555 318 7730
          <svg viewBox="0 0 16 16"><path d="M4 1h8v14H4zM5.5 3v9h5V3z"/></svg></li>
        <li>555 402 6615
          <svg viewBox="0 0 16 16"><path d="M4 1h6v4H4zM2 6h12v8H2z"/></svg></li>
        <li class="email">office@haskelllaw.com
          <svg viewBox="0 0 16 16"><path d="M1 3h14v10H1zM2 4l6 5 6-5z"/></svg></li>
      </ul>
    </div>

    <div class="firm">
      <p class="firm-small">Law Offices of</p>
      <p class="firm-name">Tobin Haskell, PA</p>
    </div>

    <div class="edge"></div>
    <div class="web-tab">www.haskelllaw.com</div>
  </section>
</body>
</html>
```